VRP Nail Gel Polish Color Tip Swatch Label Design for SUN RAY collection

We need a label design for the color swatch that will go with our new collection of nail gel polish called SUN RAY. We are a nail and beauty supply distributor in the US selling to retail nail salons in the US only. Please also see our other project launched today: VRP Gel Nail Polish Collection for 15 ml bottle (Contest)

Target Market(s)

Retail Nail Salons in the US

Industry/Entity Type

Nail Salon

Font styles to use
Serif
Sans Serif

Colors

Designer to choose colors to be used in the design.

Requirements
Must have
• VRP Logo - this needs to be changed to all black color for letters VRP and matte gold drop for the "drop";
• SUN RAY in big font/easy to see;
• Numbers in big font/easy to see: CA1, CA2, .... CA16 on on side; and CA17, CA18, .... CA32 on the other side (as there will be 16 nail tips on each side).
• Label dimensions must be 1.875" x 9.0".
Nice to have
• possible additional wording, "Premium gel polish", "Collection"
Should not have
• no picture of SUN RAY; no overpowering graphics to make it look too busy

```html
<!DOCTYPE html>
<html lang="en">
<head>
<meta charset="UTF-8">
<title>VRP Sun Ray Swatch Label</title>
<link href="https://fonts.googleapis.com/css2?family=Bodoni+Moda:opsz,wght@6..96,400&family=Open+Sans:wght@400;600&display=swap" rel="stylesheet">
<style>
  :root {
    --paper: #ffffff;
    --ink: #111111;
    --label-ink: #222222;
    --wave-light: #e4f7ff;
    --wave-cyan: #6fd6f5;
    --wave-blue: #5aa2f0;
    --wave-deep: #4a7fe8;
  }
  html, body {
    margin: 0;
    padding: 0;
    overflow: hidden;
    background: var(--paper);
  }
  .label {
    position: relative;
    width: 1200px;
    height: 251px;
    background: var(--paper);
    overflow: hidden;
  }
  .wave-band {
    position: absolute;
    left: 0;
    top: 46px;
    width: 1200px;
    height: 163px;
    background:
      radial-gradient(ellipse 420px 90px at 230px 70px, rgba(74,127,232,0.45), transparent 70%),
      radial-gradient(ellipse 380px 70px at 1000px 95px, rgba(74,127,232,0.45), transparent 70%),
      radial-gradient(ellipse 300px 60px at 640px 120px, rgba(90,162,240,0.35), transparent 70%),
      linear-gradient(180deg, var(--wave-cyan) 0%, var(--wave-light) 45%, var(--wave-cyan) 75%, var(--wave-light) 100%);
    opacity: 0.9;
  }
  .shade-number {
    position: absolute;
    left: calc(44.4px + 73.1px * var(--i));
    width: 60px;
    height: 16px;
    margin-left: -30px;
    margin-top: -8px;
    text-align: center;
    font-family: "Open Sans", sans-serif;
    font-size: 12.5px;
    line-height: 16px;
    letter-spacing: 0.5px;
    color: var(--label-ink);
    transform: rotate(-90deg);
  }
  .shade-number.top { top: 28px; }
  .shade-number.bottom { top: 213px; }
  .brand {
    position: absolute;
    top: 112px;
    width: 70px;
    margin-left: -35px;
    text-align: center;
    font-family: "Open Sans", sans-serif;
    font-weight: 600;
    font-size: 20px;
    line-height: 24px;
    letter-spacing: 1px;
    color: var(--ink);
  }
  .brand.left { left: 48px; }
  .brand.right { left: 1140px; }
  .title {
    position: absolute;
    left: 624px;
    top: 70px;
    transform: translateX(-50%);
    margin: 0;
    white-space: nowrap;
    font-family: "Bodoni Moda", serif;
    font-weight: 400;
    font-size: 92px;
    line-height: 90px;
    font-variant: small-caps;
    color: var(--ink);
  }
  .tagline {
    position: absolute;
    left: 624px;
    top: 159px;
    transform: translateX(-50%);
    margin: 0;
    padding-left: 17px;
    white-space: nowrap;
    font-family: "Open Sans", sans-serif;
    font-size: 13px;
    line-height: 16px;
    letter-spacing: 17px;
    font-variant: small-caps;
    color: var(--ink);
  }
</style>
</head>
<body>
  <div class="label">
    <div class="wave-band" role="img" aria-label="Flowing blue and cyan wave ribbons across the label"></div>

    <div class="shade-number top" style="--i:0">CA17</div>
    <div class="shade-number top" style="--i:1">CA18</div>
    <div class="shade-number top" style="--i:2">CA19</div>
    <div class="shade-number top" style="--i:3">CA20</div>
    <div class="shade-number top" style="--i:4">CA21</div>
    <div class="shade-number top" style="--i:5">CA22</div>
    <div class="shade-number top" style="--i:6">CA23</div>
    <div class="shade-number top" style="--i:7">CA24</div>
    <div class="shade-number top" style="--i:8">CA25</div>
    <div class="shade-number top" style="--i:9">CA26</div>
    <div class="shade-number top" style="--i:10">CA27</div>
    <div class="shade-number top" style="--i:11">CA28</div>
    <div class="shade-number top" style="--i:12">CA29</div>
    <div class="shade-number top" style="--i:13">CA30</div>
    <div class="shade-number top" style="--i:14">CA31</div>
    <div class="shade-number top" style="--i:15">CA32</div>

    <div class="brand left">VRP</div>
    <div class="brand right">VRP</div>

    <h1 class="title">Sun Ray</h1>
    <p class="tagline">Premium gel polish</p>

    <div class="shade-number bottom" style="--i:0">CA1</div>
    <div class="shade-number bottom" style="--i:1">CA2</div>
    <div class="shade-number bottom" style="--i:2">CA3</div>
    <div class="shade-number bottom" style="--i:3">CA4</div>
    <div class="shade-number bottom" style="--i:4">CA5</div>
    <div class="shade-number bottom" style="--i:5">CA6</div>
    <div class="shade-number bottom" style="--i:6">CA7</div>
    <div class="shade-number bottom" style="--i:7">CA8</div>
    <div class="shade-number bottom" style="--i:8">CA9</div>
    <div class="shade-number bottom" style="--i:9">CA10</div>
    <div class="shade-number bottom" style="--i:10">CA11</div>
    <div class="shade-number bottom" style="--i:11">CA12</div>
    <div class="shade-number bottom" style="--i:12">CA13</div>
    <div class="shade-number bottom" style="--i:13">CA14</div>
    <div class="shade-number bottom" style="--i:14">CA15</div>
    <div class="shade-number bottom" style="--i:15">CA16</div>
  </div>
</body>
</html>
```